Business Card Design

We Need a business card design for my company based in Tv Radio and music Productions and hunt Talent.

Industry/Entity Type

Business

Contact Information for Business Card

BrentaVue Production's, Teodor Vignoles,Cell Phone 318 4957310
Musician, Productor, Hunt Talent. Miami Fla. www.brentavue.net Mail. teodorvignoles@mailvana.com

```html
<!DOCTYPE html>
<html lang="en">
<head>
<meta charset="utf-8">
<title>BrentaVue Production's – Business Card</title>
<link rel="stylesheet" href="https://fonts.googleapis.com/css2?family=Comfortaa:wght@500;600&family=Righteous&display=swap">
<style>
  :root {
    --burst-core: #fffbe0;
    --burst-yellow: #ffd21f;
    --burst-amber: #fbb41c;
    --burst-orange: #f18a1f;
    --brand-red: #8e2b1b;
    --ink: #111111;
  }
  html, body {
    margin: 0;
    padding: 0;
    width: 1200px;
    height: 702px;
    overflow: hidden;
  }
  .card {
    position: relative;
    width: 1200px;
    height: 702px;
    overflow: hidden;
  }
  .card__backdrop {
    position: absolute;
    inset: 0;
    background: radial-gradient(ellipse 62% 70% at 50% 50%,
      var(--burst-core) 0%,
      var(--burst-yellow) 28%,
      var(--burst-amber) 60%,
      var(--burst-orange) 100%);
  }
  .card__line {
    position: absolute;
    left: 0;
    width: 100%;
    margin: 0;
    text-align: center;
    line-height: 1;
    white-space: nowrap;
  }
  .brand-name {
    top: 122px;
    font-family: "Righteous", sans-serif;
    font-size: 68px;
    color: var(--brand-red);
    letter-spacing: 1px;
  }
  .contact {
    font-family: "Comfortaa", sans-serif;
    font-weight: 600;
    color: var(--ink);
  }
  .contact--name   { top: 232px; font-size: 48px; }
  .contact--role   { top: 294px; font-size: 42px; }
  .contact--phone  { top: 347px; font-size: 42px; }
  .contact--email  { top: 400px; font-size: 42px; }
  .contact--city   { top: 456px; font-size: 42px; }
  .web-address {
    top: 528px;
    font-family: "Righteous", sans-serif;
    font-size: 78px;
    color: var(--brand-red);
    letter-spacing: 1px;
  }
</style>
</head>
<body>
  <main class="card">
    <div class="card__backdrop" role="img" aria-label="Orange and yellow light burst with glowing bokeh circles"></div>
    <h1 class="card__line brand-name">BrentaVue Production's</h1>
    <p class="card__line contact contact--name">Teodor Vignoles</p>
    <p class="card__line contact contact--role">Musician, Productor, Hunt Talent</p>
    <p class="card__line contact contact--phone">Cell Phone 318 4957310Mail.</p>
    <p class="card__line contact contact--email">teodorvignoles@mailvana.com</p>
    <p class="card__line contact contact--city">Miami Fla</p>
    <p class="card__line web-address">www.brentavue.net</p>
  </main>
</body>
</html>
```